Rollers & Glides.com

Vertical Business Card with focus on branding with our icon. Information on card will be logo, persons name, position, phone number, email address and website. Use the the name Marcus Tilden, position President, phone number 555.214.8890, email Marcus@rollersandglides.com, website www.rollersandglides.com.

```html
<!DOCTYPE html>
<html lang="en">
<head>
<meta charset="utf-8">
<title>Rollers &amp; Glides.com — Business Card</title>
<link rel="stylesheet" href="https://fonts.googleapis.com/css2?family=Montserrat:wght@400;600;700&display=swap">
<style>
  :root {
    --backdrop: #e9e6e1;
    --card: #fbfbfb;
    --brand-blue: #1f4fa8;
    --ink: #4a4a4a;
    --ink-strong: #3a3a3a;
  }
  * { margin: 0; padding: 0; box-sizing: border-box; }
  html, body {
    width: 1200px;
    height: 1141px;
    overflow: hidden;
    background: var(--backdrop);
    font-family: "Montserrat", sans-serif;
  }
  .business-card {
    position: absolute;
    left: 310px;
    top: 63px;
    width: 580px;
    height: 1015px;
    background: var(--card);
    box-shadow: 0 6px 22px rgba(0, 0, 0, 0.12);
    display: flex;
    flex-direction: column;
    align-items: center;
    text-align: center;
  }
  .brand {
    margin-top: 250px;
    display: flex;
    align-items: center;
    gap: 16px;
  }
  .brand-dot {
    width: 26px;
    height: 26px;
    border-radius: 50%;
    background: var(--brand-blue);
  }
  .brand-name {
    font-weight: 700;
    font-size: 36px;
    color: var(--brand-blue);
    letter-spacing: 0.5px;
  }
  .person-name {
    margin-top: 210px;
    font-weight: 700;
    font-size: 40px;
    color: var(--brand-blue);
    text-transform: uppercase;
    letter-spacing: 0.5px;
  }
  .person-role {
    margin-top: 2px;
    font-weight: 600;
    font-size: 28px;
    color: var(--ink-strong);
  }
  .contact-icons {
    margin-top: 26px;
    display: flex;
    gap: 10px;
  }
  .contact-icon {
    width: 34px;
    height: 34px;
    border-radius: 50%;
    background: var(--brand-blue);
    display: flex;
    align-items: center;
    justify-content: center;
  }
  .contact-line {
    font-weight: 400;
    font-size: 29px;
    color: var(--ink);
    line-height: 1.35;
  }
  .contact-phone { margin-top: 30px; }
  .divider {
    width: 62px;
    height: 5px;
    background: var(--brand-blue);
    margin: 22px 0 18px;
  }
</style>
</head>
<body>
  <main class="business-card">
    <div class="brand">
      <span class="brand-dot"></span>
      <span class="brand-name">Rollers &amp; Glides.com</span>
    </div>

    <h1 class="person-name">Marcus Tilden</h1>
    <p class="person-role">President</p>

    <div class="contact-icons">
      <span class="contact-icon" aria-label="Phone">
        <svg width="18" height="18" viewBox="0 0 24 24" fill="#fff">
          <path d="M6.6 10.8a15.1 15.1 0 0 0 6.6 6.6l2.2-2.2a1 1 0 0 1 1-.25 11.4 11.4 0 0 0 3.6.57 1 1 0 0 1 1 1V20a1 1 0 0 1-1 1A17 17 0 0 1 3 4a1 1 0 0 1 1-1h3.5a1 1 0 0 1 1 1c0 1.25.2 2.45.57 3.6a1 1 0 0 1-.25 1z"/>
        </svg>
      </span>
      <span class="contact-icon" aria-label="Email">
        <svg width="20" height="20" viewBox="0 0 24 24" fill="none" stroke="#fff" stroke-width="1.8">
          <rect x="3" y="6" width="18" height="12" rx="1"/>
          <path d="M3 7l9 6 9-6"/>
        </svg>
      </span>
    </div>

    <p class="contact-line contact-phone">555.214.8890</p>
    <p class="contact-line contact-email">Marcus@rollersandglides.com</p>
    <span class="divider"></span>
    <p class="contact-line contact-web">www.rollersandglides.com</p>
  </main>
</body>
</html>
```